Student Card

we are college and require a student card which we issue on enlroment to students, just like a univeristy.

Baisic information need to be placed is:
Student photo
student ID
date of birth
exp date

our college contact details on the rear
its a tool for branding so its important the theme is in line with our colours and logo, please view our website www.hartwellcollege.net.au

Industry/Entity Type

College

```html
<!DOCTYPE html>
<html lang="en">
<head>
<meta charset="utf-8">
<title>Hartwell College – Student Card</title>
<link rel="stylesheet" href="https://fonts.googleapis.com/css2?family=Tinos:wght@700&family=Source+Sans+3:ital,wght@0,400;0,600;1,700&display=swap">
<style>
  :root {
    --page: #ffffff;
    --teal-light: #6cc4d2;
    --teal: #58b7c7;
    --teal-deep: #4aa9ba;
    --royal: #4455a5;
    --ink: #1f1f1f;
    --stripe: #231f20;
    --white: #ffffff;
    --serif: "Tinos", "Times New Roman", serif;
    --sans: "Source Sans 3", "Myriad Pro", sans-serif;
  }
  * { margin: 0; padding: 0; box-sizing: border-box; }
  html, body { width: 1200px; height: 1000px; overflow: hidden; background: var(--page); }
  .canvas { position: relative; width: 1200px; height: 1000px; }

  /* Front of card */
  .card-front {
    position: absolute; left: 260px; top: 44px; width: 676px; height: 392px;
    border-radius: 10px; overflow: hidden;
  }
  .card-front__texture {
    position: absolute; inset: 0;
    background: radial-gradient(ellipse at 30% 40%, var(--teal-light), var(--teal) 55%, var(--teal-deep));
  }
  .college-name {
    position: absolute; left: 14px; top: 32px;
    font-family: var(--serif); font-weight: 700; font-size: 36px; letter-spacing: 0;
    color: var(--ink); line-height: 1; white-space: nowrap;
  }
  .college-faculties {
    position: absolute; left: 33px; top: 71px;
    font-family: var(--sans); font-style: italic; font-weight: 700; font-size: 18.5px;
    color: var(--ink); white-space: nowrap;
  }
  .photo-frame { position: absolute; left: 424px; top: 12px; width: 250px; height: 300px; }
  .photo-label {
    position: absolute; left: 420px; top: 122px; width: 254px; text-align: center;
    font-family: var(--serif); font-weight: 700; font-size: 19px; color: var(--ink);
  }
  .student-name {
    position: absolute; left: 343px; top: 265px;
    font-family: var(--serif); font-weight: 700; font-size: 32.5px; color: var(--ink);
  }
  .id-band {
    position: absolute; left: 0; bottom: 0; width: 100%; height: 70px;
    background: var(--royal); color: var(--white); font-family: var(--sans);
  }
  .id-band__title { position: absolute; left: 24px; top: 0; font-weight: 600; font-size: 33px; line-height: 1.2; }
  .id-band__dob { position: absolute; left: 25px; top: 40px; font-style: italic; font-weight: 700; font-size: 18.5px; line-height: 1.2; }
  .id-band__expiry { position: absolute; right: 18px; top: 34px; font-style: italic; font-weight: 700; font-size: 18.5px; line-height: 1.2; }

  /* Back of card */
  .card-back {
    position: absolute; left: 260px; top: 557px; width: 676px; height: 391px;
    border: 1px solid var(--ink); border-radius: 14px; overflow: hidden; background: var(--white);
  }
  .mag-stripe { position: absolute; left: 0; top: 50px; width: 100%; height: 55px; background: var(--stripe); }
  .brand-mark {
    position: absolute; left: 0; top: 226px; width: 100%;
    display: flex; justify-content: center; align-items: center; gap: 10px;
  }
  .brand-mark__square { width: 18px; height: 18px; background: var(--royal); }
  .brand-mark__name { font-family: var(--serif); font-weight: 700; font-size: 20px; color: var(--royal); }
  .contact-phone {
    position: absolute; left: 0; top: 277px; width: 100%; text-align: center;
    font-family: var(--sans); font-weight: 600; font-size: 55px; color: var(--royal); line-height: 1;
  }
  .contact-email {
    position: absolute; left: 0; top: 343px; width: 100%; text-align: center;
    font-family: var(--sans); font-weight: 400; font-size: 26.5px; color: var(--ink); line-height: 1;
  }
</style>
</head>
<body>
<main class="canvas">
  <section class="card-front" aria-label="Student card, front">
    <div class="card-front__texture" role="img" aria-label="Textured teal card background"></div>
    <h1 class="college-name">HARTWELL COLLEGE</h1>
    <p class="college-faculties">Hospitality, Tourism, Business &amp; Management</p>
    <svg class="photo-frame" viewBox="0 0 250 300" aria-hidden="true">
      <path d="M18 6 Q125 12 232 6 Q244 6 242 20 Q252 180 126 296 Q0 180 8 20 Q6 6 18 6 Z"
            fill="#ffffff" stroke="#4455a5" stroke-width="9" stroke-linejoin="round"/>
    </svg>
    <p class="photo-label">[Photo Goes Here]</p>
    <p class="student-name">Jane Doe</p>
    <div class="id-band">
      <p class="id-band__title">Student ID</p>
      <p class="id-band__dob">DOB: 00/00/0000</p>
      <p class="id-band__expiry">exp date: 00/00/0000</p>
    </div>
  </section>

  <section class="card-back" aria-label="Student card, back">
    <div class="mag-stripe"></div>
    <div class="brand-mark">
      <span class="brand-mark__square"></span>
      <span class="brand-mark__name">HARTWELL COLLEGE</span>
    </div>
    <p class="contact-phone">Call: 617.3484.2261</p>
    <p class="contact-email">Email: info@hartwellcollege.net.au</p>
  </section>
</main>
</body>
</html>
```